Core Value Graphic for a Service Disabled and Minority Certified contractor

My company, Keystone Aid Partners, is a US Federal Contractor that hires veterans and service disabled veterans. Our website is www.keystoneaid7.example. We work hard to maintain a 50:50 split between veterans and non-veterans on our team. Our tagline is "To Find a Better Way." We are continually looking to integrate technology and efficiency into all that we do.

I want a way to express our company core values visually so that our employees and customers alike can read them and get a sense of who we are, what drives us to succeed, and what makes up our team DNA.

I need an artist like you to help me represent our core values visually. In a manner that I can print it out on an 8"X11" sheet of paper or a large 48" X 48" poster, without losing the visual clarity or that it pixelates out of focus. I am looking for a color scheme that is patriotic with Red, White, and Blues and similar hues. I would also like to incorporate my logo and tagline into the design in some manner.

I have attached several examples of a Core Value Grids from other companies. I am hopeful it will inspire you, and a get your brain juices flowing to provide me with a knockout Core Value Grid that will rock only you can provide! I also include a copy of my company Core Values and a copy of our Logo.

Looking forward to seeing your creations. Thanks.

Target Market(s)

Employees, any potential strategic alliance partners, and customers.

Industry/Entity Type

Contractor

Requirements
Must have
• Patriotic feel and have my logo someplace on the document.

```html
<!DOCTYPE html>
<html lang="en">
<head>
<meta charset="utf-8">
<title>Our Core Values — Keystone Aid Partners</title>
<link rel="stylesheet" href="https://fonts.googleapis.com/css2?family=Montserrat:wght@800;900&family=Open+Sans:wght@500;600;700;800&display=swap">
<style>
  :root{
    --navy:#1f3f7a;
    --navy-deep:#16305f;
    --red-dark:#b01c24;
    --red:#dc2733;
    --gray:#8a8b8e;
    --white:#ffffff;
    --paper:#eeeef0;
    --stripe-gray:#cbccce;
    --stripe-red:#bd1f2a;
  }
  html,body{margin:0;padding:0;overflow:hidden;background:var(--white);}
  .canvas{
    position:relative;width:927px;height:1200px;overflow:hidden;
    background:var(--paper);
    font-family:"Open Sans",Arial,sans-serif;
  }
  .stripes{position:absolute;left:0;width:100%;}
  .stripes--gray{
    top:0;height:1200px;
    background:repeating-linear-gradient(to bottom,
      #e6e6e8 0 9px,#ffffff 9px 13px,var(--stripe-gray) 13px 17px,#f4f4f5 17px 24px,#9fa0a3 24px 26px,#f1f1f2 26px 33px);
  }
  .stripes--red{
    top:0;height:340px;
    background:repeating-linear-gradient(to bottom,
      #ffffff 0 8px,var(--stripe-red) 8px 13px,#ffffff 13px 20px,#a8161f 20px 28px,#f3f3f3 28px 34px);
  }
  .stripes--navy{
    top:1010px;height:190px;opacity:.85;
    background:repeating-linear-gradient(to bottom,
      #f2f2f3 0 7px,var(--navy) 7px 12px,#ffffff 12px 18px,var(--navy-deep) 18px 21px);
  }

  /* rotated working plane */
  .stage{position:absolute;left:0;top:0;width:1px;height:1px;transform:rotate(-15deg);transform-origin:0 0;}
  .ribbons{position:absolute;left:-400px;top:0;width:2100px;height:1500px;overflow:visible;}

  .title{position:absolute;margin:0;color:var(--navy);font-family:"Montserrat",Arial,sans-serif;font-weight:900;
    line-height:1;white-space:nowrap;
    text-shadow:0 3px 0 var(--white),3px 0 0 var(--white),-3px 0 0 var(--white),0 -3px 0 var(--white),4px 7px 8px rgba(0,0,0,.35);}
  .title__our{left:-20px;top:100px;font-size:58px;letter-spacing:-2px;}
  .title__main{left:-32px;top:143px;font-size:80px;letter-spacing:-3px;}

  .band-title{position:absolute;height:80px;line-height:80px;color:var(--white);font-weight:700;font-size:31px;
    white-space:nowrap;letter-spacing:-.2px;text-shadow:1px 2px 3px rgba(0,0,0,.25);}

  .col-text{position:absolute;width:119px;text-align:center;color:var(--white);}
  .col-text h3{margin:0 0 3px;font-weight:800;font-size:17px;line-height:15px;text-transform:uppercase;letter-spacing:-.3px;}
  .col-text p{margin:0 0 12px;font-weight:500;font-size:11.5px;line-height:15px;}
  .col-text strong{font-weight:800;}

  .tagline{position:absolute;left:-262px;top:1143px;height:44px;line-height:44px;color:var(--white);
    font-weight:800;font-size:36px;white-space:nowrap;letter-spacing:-.5px;}

  .brand{position:absolute;left:-232px;top:1052px;display:flex;align-items:center;gap:10px;}
  .brand__mark{width:26px;height:26px;background:var(--stripe-red);}
  .brand__name{color:var(--navy);font-weight:800;font-size:33px;line-height:1;white-space:nowrap;letter-spacing:-.5px;}
</style>
</head>
<body>
<main class="canvas">
  <div class="stripes stripes--gray"></div>
  <div class="stripes stripes--red"></div>
  <div class="stripes stripes--navy"></div>

  <div class="stage">
    <svg class="ribbons" viewBox="-400 0 2100 1500" aria-hidden="true">
      <defs>
        <filter id="ribbon-shadow" x="-20%" y="-20%" width="140%" height="140%">
          <feDropShadow dx="3" dy="5" stdDeviation="5" flood-color="#000" flood-opacity=".35"/>
        </filter>
        <linearGradient id="col-red-dark" x1="0" y1="0" x2="0" y2="1"><stop offset="0" stop-color="#a81a22"/><stop offset="1" stop-color="#861118"/></linearGradient>
        <linearGradient id="col-red" x1="0" y1="0" x2="0" y2="1"><stop offset="0" stop-color="#d42531"/><stop offset="1" stop-color="#b31b26"/></linearGradient>
        <linearGradient id="band-gray" x1="0" y1="0" x2="1" y2="0"><stop offset="0" stop-color="#7a7b7e"/><stop offset=".4" stop-color="#b9babd"/><stop offset="1" stop-color="#d4d5d7"/></linearGradient>
        <linearGradient id="col-gray" x1="0" y1="0" x2="0" y2="1"><stop offset="0" stop-color="#88898c"/><stop offset="1" stop-color="#5c5d60"/></linearGradient>
        <linearGradient id="col-teal" x1="0" y1="0" x2="0" y2="1"><stop offset="0" stop-color="#1c5290"/><stop offset=".55" stop-color="#1a7aa0"/><stop offset="1" stop-color="#1c93a6"/></linearGradient>
        <linearGradient id="col-navy" x1="0" y1="0" x2="0" y2="1"><stop offset="0" stop-color="#1f3c76"/><stop offset="1" stop-color="#2c5595"/></linearGradient>
      </defs>

      <!-- tagline band -->
      <rect x="-400" y="1135" width="1300" height="60" fill="var(--navy-deep)"/>

      <!-- value 1 -->
      <g filter="url(#ribbon-shadow)">
        <path d="M-77,267 Q-77,222 -32,222 H1700 V302 H58 V1000 L-77,955 Z" fill="var(--red-dark)"/>
        <path d="M-77,302 H58 V1000 L-77,955 Z" fill="url(#col-red-dark)"/>
      </g>
      <!-- value 2 -->
      <g filter="url(#ribbon-shadow)">
        <path d="M63,357 Q63,312 108,312 H1700 V392 H198 V1098 L63,1053 Z" fill="var(--red)"/>
        <path d="M63,392 H198 V1098 L63,1053 Z" fill="url(#col-red)"/>
      </g>
      <!-- value 3 -->
      <g filter="url(#ribbon-shadow)">
        <path d="M203,447 Q203,402 248,402 H1700 V482 H338 V1201 L203,1156 Z" fill="url(#band-gray)"/>
        <path d="M203,482 H338 V1201 L203,1156 Z" fill="url(#col-gray)"/>
      </g>
      <!-- value 4 -->
      <g filter="url(#ribbon-shadow)">
        <path d="M343,537 Q343,492 388,492 H1700 V572 H478 V1281 L343,1236 Z" fill="#1c4f8f"/>
        <path d="M343,572 H478 V1281 L343,1236 Z" fill="url(#col-teal)"/>
      </g>
      <!-- value 5 -->
      <g filter="url(#ribbon-shadow)">
        <path d="M483,627 Q483,582 528,582 H1700 V662 H618 V1298 L483,1253 Z" fill="#1b3870"/>
        <path d="M483,662 H618 V1298 L483,1253 Z" fill="url(#col-navy)"/>
      </g>
    </svg>

    <h1 class="title title__our">OUR</h1>
    <h1 class="title title__main">CORE VALUES</h1>

    <div class="band-title" style="left:-15px;top:222px;">Everyone comes back to the Green Zone.</div>
    <div class="band-title" style="left:125px;top:312px;">Never leave your wingman.</div>
    <div class="band-title" style="left:265px;top:402px;">Fail quickly and learn.</div>
    <div class="band-title" style="left:405px;top:492px;">Boldly go. Seek. Find.</div>
    <div class="band-title" style="left:545px;top:582px;">Troops eat first.</div>

    <section class="col-text" style="left:-69px;top:330px;">
      <h3>What it means</h3>
      <p>Safety takes precedence over every phase of the day's operation.</p>
      <h3>How to express it</h3>
      <p>Anyone can call a stop to the work in progress if an unsafe act is occurring. In fact, it is each team member's duty to do so, rectify the unsafe issue, then proceed. Never hesitate; everyone comes back. Finally, each After Action Review begins with discussing safety issues. We always let everyone on the team know of an unsafe situation, so it can be avoided in the future.</p>
      <h3>Result</h3>
      <p>All team members go home to their loved ones each day to pursue their individual happiness.</p>
    </section>

    <section class="col-text" style="left:71px;top:420px;">
      <h3>What it means</h3>
      <p>We always help your team members to be successful. Commitment to each other and to our own personal integrity is the fuel that empowers us.</p>
      <h3>How to express it</h3>
      <p>If a Wingman is having challenges accomplishing their individual priorities or completing their assigned mission, volunteer to help them to do so. This goes for Subs/Suppliers as well. We help those who help us succeed! Always look to establish the best win-win relationship possible, and do what you can to support them if they get into a bind.</p>
      <h3>Result</h3>
      <p>Be there for them and they will be there for us.</p>
    </section>

    <section class="col-text" style="left:211px;top:512px;">
      <h3>What it means</h3>
      <p>If you're not making mistakes, you're not taking enough chances or getting out of your comfort zone.</p>
      <h3>How to express it</h3>
      <p>Use your best judgment when trying something new. But, don't let your pride keep you from saying, <strong>"I was wrong"</strong> when your idea doesn't work. We trust you will know when it's time to dump the idea, or stop doing something that doesn't work.</p>
      <h3>Result</h3>
      <p>No one will ever be penalized you for making a mistake. Don't be afraid to try something you believe will work. That's how we grow ourselves and our team members.</p>
    </section>

    <section class="col-text" style="left:351px;top:602px;">
      <h3>What it means</h3>
      <p>We weave innovation into the fabric that makes up our company.</p>
      <h3>How to express it</h3>
      <p>We're early adopters of technology. We quickly evaluate new technologies or processes that could separate us from our competition. Then we implement and evaluate these new technologies. We dump it quickly if we see it is not helping us achieve "Commander's Intent". We have the guts to be first. We iterate continuously and attack, attack, attack.</p>
      <h3>Result</h3>
      <p>We will be ahead of our competition. It's one mechanism that helps us scale. Prosperity favors the bold!</p>
    </section>

    <section class="col-text" style="left:491px;top:692px;">
      <h3>What it means</h3>
      <p>No leader will put themselves ahead of their subordinates.</p>
      <h3>How to express it</h3>
      <p>We lead by example. Demonstrate the moral courage and discipline to do the right thing at the highest level of quality.</p>
      <h3>Result</h3>
      <p>Every new team member will quickly realize their leaders genuinely care for their welfare and success. This is the best way to drive Esprit de Corps and achieve excellence.</p>
    </section>

    <div class="brand">
      <span class="brand__mark"></span>
      <span class="brand__name">Keystone Aid Partners</span>
    </div>

    <div class="tagline">“TO FIND A BETTER WAY”</div>
  </div>
</main>
</body>
</html>
```